Greek Yogurt Design

Design Brief – Premium Greek Yogurt Line (150g Pot)
Background
We are a small-to-medium dairy producer launching a new premium Greek yogurt range. This line will come in slightly larger pots than our standard yogurts, and we are targeting an upmarket clientele with a higher price point.
Product Details
Product: Greek Yogurt (fruit on the bottom, yogurt on top)
Flavours:
Natural
Strawberry
Forest Fruit
Peach & Apricot
Vanilla
Mango
Weight: 150g
Kosher Certification: 2 logos must be applied neatly (logos provided).
Lid: Standard universal lid (not flavour-specific).
Design Style
Clean, elegant, and premium feel (avoid clutter).
Should stand out as sophisticated compared to our standard range.
Visual hierarchy:
Brand & product type (Greek Yogurt) should be clear.
Flavour indicated with subtle but distinct cues (colour palette, fruit illustration/photography).
“Fruit on the bottom” message should be communicated simply.
Premium cues: minimalist typography, restrained colour palette, elegant fruit imagery.
References / Inspiration
Velmora Yogurt
– clean, bold, dairy-traditional.
Brask Dairy Greek Style
– natural, elegant design.
Lunaro Greek Yogurt
– modern, colourful yet clean.
Deliverables
Pot sleeve / pot design (to wrap around container).
Must work across all flavours with colour/flavour variation.
Space for universal lid (do not design individual lids).
Application of 2 kosher logos in a balanced way.
Updates
Industry/Entity Type
Dairy
Colors
Designer to choose colors to be used in the design.
Look and feel
Each slider illustrates characteristics of the customer's brand and the style your logo design should communicate.

```html
<!DOCTYPE html>
<html lang="en">
<head>
<meta charset="utf-8">
<title>Doveli Greek Yogurt – Forest Fruits Pot Sleeve</title>
<link rel="stylesheet" href="https://fonts.googleapis.com/css2?family=Fraunces:opsz,wght@9..144,300;9..144,400&family=Quicksand:wght@500;700&display=swap">
<style>
  :root {
    --backdrop: #d9dadf;
    --sleeve: #f4f4f5;
    --rim-dark: #1d1b3a;
    --rim-mid: #3a3760;
    --ink: #2a2a2e;
    --navy: #24223f;
    --brand-green: #5cc14a;
    --berry-deep: #1f1d4a;
    --berry-mid: #3b3a86;
    --leaf: #4f8a2e;
    --leaf-light: #8cbf55;
    --raspberry: #c23a5a;
  }
  * { box-sizing: border-box; margin: 0; padding: 0; }
  html, body {
    width: 1200px; height: 900px; overflow: hidden;
    background: var(--backdrop);
  }
  .canvas {
    position: relative; width: 1200px; height: 900px;
    display: flex; align-items: center; justify-content: center;
  }
  .sleeve {
    position: relative; width: 1000px; height: 500px;
    background: var(--sleeve);
    box-shadow: 0 18px 40px rgba(40, 40, 60, 0.12);
    overflow: hidden;
  }
  .sleeve__rim {
    position: absolute; left: 0; top: 0; width: 100%; height: 46px;
    background: linear-gradient(180deg, var(--rim-dark) 0%, var(--rim-mid) 55%, var(--rim-dark) 100%);
  }
  .brand {
    position: absolute; left: 90px; top: 92px;
    display: flex; flex-direction: column; gap: 2px;
  }
  .brand__row { display: flex; align-items: center; gap: 10px; }
  .brand__dot {
    width: 22px; height: 22px; border-radius: 50%;
    background: var(--brand-green);
  }
  .brand__name {
    font-family: "Quicksand", sans-serif; font-weight: 700;
    font-size: 34px; color: var(--brand-green); letter-spacing: 0.5px;
  }
  .brand__tagline {
    font-family: "Quicksand", sans-serif; font-weight: 500;
    font-size: 13px; color: var(--brand-green); padding-left: 32px;
  }
  .product-title {
    position: absolute; left: 84px; top: 168px;
    font-family: "Fraunces", serif; font-weight: 300;
    font-size: 118px; line-height: 0.92; color: var(--ink);
    letter-spacing: -1px;
  }
  .flavour-tag {
    position: absolute; left: 90px; top: 394px;
    background: var(--navy); color: #fff;
    font-family: "Quicksand", sans-serif; font-weight: 700;
    font-size: 17px; padding: 5px 16px 6px;
  }
  .claim {
    position: absolute; left: 90px; top: 438px;
    font-family: "Quicksand", sans-serif; font-weight: 500;
    font-size: 17px; color: var(--ink);
  }
  .fruit-art {
    position: absolute; right: 60px; top: 70px; width: 470px; height: 430px;
  }
</style>
</head>
<body>
  <main class="canvas">
    <section class="sleeve" aria-label="Greek yogurt pot sleeve, forest fruits flavour">
      <div class="sleeve__rim"></div>

      <div class="brand">
        <div class="brand__row">
          <span class="brand__dot"></span>
          <span class="brand__name">Doveli</span>
        </div>
        <span class="brand__tagline">Pure Goodness</span>
      </div>

      <h1 class="product-title">Greek<br>Yogurt</h1>

      <p class="flavour-tag">Forest Fruits</p>
      <p class="claim">Fruit on the bottom, yogurt on top</p>

      <svg class="fruit-art" viewBox="0 0 470 430" role="img"
           aria-label="Illustration of a glossy blackberry with green leaves, dew drops and a small raspberry">
        <defs>
          <radialGradient id="fruitTones" cx="55%" cy="45%" r="60%">
            <stop offset="0%" stop-color="var(--berry-mid)"/>
            <stop offset="45%" stop-color="var(--berry-deep)"/>
            <stop offset="70%" stop-color="var(--leaf)"/>
            <stop offset="100%" stop-color="var(--sleeve)" stop-opacity="0"/>
          </radialGradient>
        </defs>
        <rect width="470" height="430" fill="url(#fruitTones)"/>
      </svg>
    </section>
  </main>
</body>
</html>
```